Vireon Spool Business Card Design

This is a start up company that has state of the art patented technology for turbo chargers,that can be used on engines, gas or diesel, for any type of automotive,aviation,marine or industrial purpose.
This technology will provide longer life,lower maintenance and better performance and help produce lower emissions with any turbocharged engine.Red would be a predominate color and the design should communicate the latest technology,economy and
Environmental concern.
This product will initially be distributed in the U.S.A. But should move rapidly to global use.
Updates

Thank you for your design submissions, I have increased the budget for this job because my initial order was too low for the quality of work shown, plus I would Like to see some more options. I have a meeting this Sunday with my other partners and would anticipate being able to give you some feedback by the Beginning of next week. Regards.

Thank you for everyone's participation. The deadline is still open until 6/15 and my partners and I have a meeting Scheduled this weekend. At this time we have not ruled anyone out, But will be making a decision during the course of our meeting and wil Decide which direction we will be going in by the beginning of the week. Thanks again, regards, Tom Brandt.

Hello everybody, Sorry for the delay in communication, we have been very busy in putting the start up together. We are still not decided on the design of the business card and have a wide range to choose from. I would anticipated we shall have an answer within the next two weeks. Regards, Tom Brandt.

Target Market(s)

Manufacturers and wholesalers' of OEM and replacement turbochargers

Industry/Entity Type

Industrial

Contact Information for Business Card

We need a logo that should incorporate the " Vireon, a " possibly super imposed over a turbo charger with the fan blades of the turbocharger showing in the center of the "a" .
Name,title,phone number and email address only, no street/mailing address at this time.
The full name of the company is
" Vireon Spool Dynamics LLC "
For the initial card you can use my info.
Thomas Brandt
VP Sales & Marketing
tbrandt@vireonspooldyn.example
555 014 2286

Requirements
Must have
• The Vireon A, the outline of a turbo charger
Nice to have
• Something classy and simple and worldly (global)
Should not have
• No engines,cars,boats,planes

```html
<!DOCTYPE html>
<html lang="en">
<head>
<meta charset="utf-8">
<title>Vireon Spool Dynamics – Business Card</title>
<link href="https://fonts.googleapis.com/css2?family=Michroma&display=swap" rel="stylesheet">
<style>
  :root {
    --page-bg: #d9d6d1;
    --card-black: #0d0d0e;
    --card-dark: #1a1a1c;
    --band-light: #4a4a4d;
    --band-dark: #2a2a2c;
    --accent-red: #e0151b;
    --text-white: #f2f2f2;
  }
  * { box-sizing: border-box; margin: 0; padding: 0; }
  html, body {
    width: 1200px;
    height: 1000px;
    overflow: hidden;
    background: var(--page-bg);
  }
  body {
    display: flex;
    align-items: center;
    justify-content: center;
    font-family: "Michroma", "Arial", sans-serif;
  }
  .business-card {
    position: relative;
    width: 900px;
    height: 514px;
    background: linear-gradient(170deg, var(--card-dark) 0%, var(--card-black) 70%);
    overflow: hidden;
    box-shadow: 0 10px 30px rgba(0,0,0,0.25);
  }
  .texture-band {
    position: absolute;
    left: 0; top: 0;
    width: 100%;
    height: 190px;
    background: linear-gradient(180deg, var(--band-light) 0%, var(--band-dark) 100%);
    border-bottom: 2px solid #565659;
  }
  .brand {
    position: absolute;
    left: 48px;
    top: 44px;
    display: flex;
    align-items: center;
    gap: 26px;
  }
  .brand-dot {
    width: 92px;
    height: 92px;
    border-radius: 50%;
    background: var(--accent-red);
    flex: none;
  }
  .brand-name {
    color: var(--text-white);
    font-size: 34px;
    line-height: 1.2;
    letter-spacing: 1px;
    text-transform: uppercase;
  }
  .brand-name .suffix { font-size: 34px; }
  .contact {
    position: absolute;
    left: 96px;
    top: 240px;
    color: var(--text-white);
  }
  .person {
    display: flex;
    align-items: baseline;
    gap: 34px;
    margin-bottom: 36px;
    text-transform: uppercase;
  }
  .person-name {
    color: var(--accent-red);
    font-size: 26px;
  }
  .person-title {
    font-size: 19px;
  }
  .contact-line {
    display: flex;
    align-items: center;
    gap: 18px;
    font-size: 17px;
    margin-bottom: 16px;
    text-transform: uppercase;
  }
  .contact-line svg { width: 22px; height: 22px; flex: none; }
</style>
</head>
<body>
  <article class="business-card">
    <div class="texture-band" role="img" aria-label="Dark carbon fibre texture band across the top of the card"></div>

    <header class="brand">
      <span class="brand-dot"></span>
      <h1 class="brand-name">Vireon Spool<br>Dynamics <span class="suffix">LLC</span></h1>
    </header>

    <section class="contact">
      <p class="person">
        <span class="person-name">Thomas Brandt</span>
        <span class="person-title">VP Sales &amp; Marketing</span>
      </p>
      <p class="contact-line">
        <svg viewBox="0 0 24 24" aria-hidden="true">
          <rect x="2" y="5" width="20" height="14" fill="var(--accent-red)"/>
          <path d="M2 5 L12 13 L22 5" fill="none" stroke="#0d0d0e" stroke-width="1.6"/>
        </svg>
        <span>tbrandt@vireonspooldyn.example</span>
      </p>
      <p class="contact-line">
        <svg viewBox="0 0 24 24" aria-hidden="true">
          <path d="M3 9 Q12 2 21 9 L18 11 L16 8 Q12 6.5 8 8 L6 11 Z" fill="var(--accent-red)"/>
          <rect x="5" y="12" width="14" height="9" rx="1.5" fill="var(--accent-red)"/>
          <circle cx="12" cy="16.5" r="2.2" fill="#0d0d0e"/>
        </svg>
        <span>555 014 2286</span>
      </p>
    </section>
  </article>
</body>
</html>
```